Presentation card Venture KELO - Tech Incubator from Perú

We need a Design to promote the incubator of technology Startups.
We are in Perú, we work with a string tech filter and develop enterprenurship competencies in the Startup team.
The card is to facilitators and staff memebers of VentureKELO.
We want a clear, modern, tech and agile Design.

We work to help New enterprises of technology here in Perú, we expect the candidates have a big competencies to Research and develop technological products.

We work using methodologies from QRB, Folmestry, Brakewell and Harrowgate univeesities. Our book base is the disciplina of enterpreneur.

We work events all year using diferent formats: Brightforge, Vorne price, OPRA Model Competition you can use these logros in your Design.

Set the name, role, email, cell phone number, address.

Example:
// Contact info section
Tobías Quiroveda
Swift Modeling Hub Manager
tobias.quiroveda@kelo-example.pe
(511) 999 000 417

// Address info section
VentureKELO
Technology-based business incubator
Av. Los Cedrales 884, Valdora
Lima - Perú
web: venture-kelo-example.org.pe
email: venture@kelo-example.pe
phone number: (511) 3926508 ext. 4418

// (optional)Lema section
Making happy using technology

// Social network section
facebook: venturekelooficial

Target Market(s)

Enterprenurship, CTO, Investors, Companies interested on open innovation services

Industry/Entity Type

Information Technology

Contact Information for Business Card

Name, Role, Email, Cell phone number

Colors

Designer to choose colors to be used in the design.

Requirements
Must have
• Logo forms and colors
Nice to have
• I add pictures of the leaders of incubator
Should not have
• No vertical designs

```html
<!DOCTYPE html>
<html lang="en">
<head>
<meta charset="utf-8">
<title>Venture KELO — Business Cards</title>
<link rel="stylesheet" href="https://fonts.googleapis.com/css2?family=Nunito+Sans:wght@400;700;800;900&family=Open+Sans:wght@400&display=swap">
<style>
  :root {
    --magenta: #bc355c;
    --ink: #1f1f22;
    --paper: #ffffff;
    --backdrop: #222427;
    --photo-a: #2c3447;
    --photo-b: #6b5a4a;
  }
  * { margin: 0; padding: 0; box-sizing: border-box; }
  html, body { width: 1200px; height: 820px; overflow: hidden; background: var(--backdrop); }
  .stage { position: relative; width: 1200px; height: 820px; }
  .card {
    position: absolute; top: 277px; width: 523px; height: 312px;
    background: var(--paper); overflow: hidden;
    font-family: "Nunito Sans", sans-serif;
  }
  .card svg.bg { position: absolute; inset: 0; }
  .card--front { left: 79px; }
  .card--back { left: 618px; }

  /* front */
  .tagline-text {
    position: absolute; left: 30px; top: 92px; line-height: 1.25;
    font-weight: 800; font-size: 19px;
  }
  .tagline-text .line1 { color: var(--ink); display: block; }
  .tagline-text .line2 { color: var(--magenta); display: block; }
  .front-contact {
    position: absolute; left: 26px; top: 162px; color: var(--paper);
    font-size: 14.5px; line-height: 1.25;
  }
  .front-contact .address { margin-bottom: 12px; }
  .front-contact .row { margin-bottom: 5px; }
  .front-contact b { font-weight: 900; }
  .social-square {
    display: inline-block; width: 11px; height: 11px; border-radius: 2px;
    background: var(--paper); margin-right: 8px; vertical-align: -1px;
  }
  .brand-front {
    position: absolute; left: 318px; top: 82px; color: var(--paper);
    font-weight: 900; font-size: 41px; line-height: 1.08; letter-spacing: -0.5px;
    white-space: nowrap;
  }

  /* back */
  .brand-back {
    position: absolute; left: 102px; top: 48px; color: var(--ink);
    font-weight: 900; font-size: 31px; line-height: 1.0;
  }
  .person {
    position: absolute; right: 16px; top: 180px; text-align: right;
  }
  .person .name { font-weight: 800; font-size: 23px; line-height: 1.1; color: var(--ink); }
  .person .name span { color: var(--magenta); }
  .person .role { font-family: "Open Sans", sans-serif; font-size: 15px; color: var(--magenta); margin-top: 2px; }
  .back-contact {
    position: absolute; right: 178px; top: 248px; text-align: right;
    font-family: "Open Sans", sans-serif; font-size: 13px; color: var(--ink); line-height: 1.6;
    white-space: nowrap;
  }
  .back-contact .phone { margin-right: 24px; }
  .motto {
    position: absolute; right: 19px; top: 250px; text-align: right;
    color: var(--paper); font-size: 14.5px; line-height: 1.15;
  }
</style>
</head>
<body>
<main class="stage">

  <section class="card card--front" aria-label="Card front">
    <svg class="bg" width="523" height="312" viewBox="0 0 523 312" aria-hidden="true">
      <path fill="var(--magenta)" d="M218,0 L523,0 L523,237 C450,288 380,305 305,312 L0,312 L0,78 C60,32 140,8 218,0 Z"/>
      <path fill="var(--paper)" d="M0,86 L243,86 C228,100 222,124 219,149 L0,149 Z"/>
    </svg>
    <p class="tagline-text">
      <span class="line1">Technology-based</span>
      <span class="line2">business incubator</span>
    </p>
    <div class="front-contact">
      <p class="address">Av. Los Cedrales 884, Valdora<br>Lima - Perú</p>
      <p class="row"><b>e:</b> venture@kelo-example.pe</p>
      <p class="row"><b>w:</b> venture-kelo-example.org.pe</p>
      <p class="row"><b>p:</b> (511) 3926508 ext. 4418</p>
      <p class="row"><span class="social-square"></span>venturekelooficial</p>
    </div>
    <h1 class="brand-front">VENTURE<br>KELO</h1>
  </section>

  <section class="card card--back" aria-label="Card back">
    <svg class="bg" width="523" height="312" viewBox="0 0 523 312" aria-hidden="true">
      <defs>
        <linearGradient id="team-tones" x1="0" y1="0" x2="1" y2="1">
          <stop offset="0" stop-color="var(--photo-a)"/>
          <stop offset="1" stop-color="var(--photo-b)"/>
        </linearGradient>
      </defs>
      <path fill="var(--magenta)" d="M0,0 L66,0 C92,60 88,118 58,152 C32,184 34,228 52,262 C68,290 90,306 103,312 L0,312 Z"/>
      <path fill="var(--magenta)" d="M359,247 L523,247 L523,287 L326,287 C340,278 352,262 359,247 Z"/>
    </svg>
    <svg class="bg" width="523" height="312" viewBox="0 0 523 312" role="img" aria-label="Group photo of the incubator team in their workspace">
      <path fill="url(#team-tones)" d="M265,0 L523,0 L523,160 C430,172 330,122 265,0 Z"/>
    </svg>
    <h2 class="brand-back">VENTURE<br>KELO</h2>
    <div class="person">
      <p class="name">Tobías <span>Quiroveda</span></p>
      <p class="role">Swift Modeling Hub Manager</p>
    </div>
    <div class="back-contact">
      <p>tobias.quiroveda@kelo-example.pe</p>
      <p class="phone">(511) 999 000 417</p>
    </div>
    <p class="motto">Making happy<br>using technology</p>
  </section>

</main>
</body>
</html>
```